Party planning business card design

Revels with Kit is a party planning business

Function Planning: Weddings/Themed Parties/Children's Parties

Adult and Children's Photo Booths
Party Themed boxes,
We can find the venue, entertainment. face painters.

Children's costumes and accessories - Sell / Hire

Web: www.revelswithkit.example
Facebook: Revels with Kit

Industry/Entity Type

Party Planning

Contact Information for Business Card

Revels With Kit, Rosalind Trevick,
Creative Director

Colors
e34297
000000

Requirements
Must have
• on my logo are you able to edit the stars to pink?

```html
<!DOCTYPE html>
<html lang="en">
<head>
<meta charset="utf-8">
<title>Revels with Kit – Business Card</title>
<link href="https://fonts.googleapis.com/css2?family=Arimo:wght@400;700&family=Great+Vibes&display=swap" rel="stylesheet">
<style>
  :root {
    --pink: #e34297;
    --pink-deep: #c9307f;
    --pink-soft: #f3a6cf;
    --white: #ffffff;
    --paper: #fbfbfb;
    --ink: #1f1f1f;
    --stage: #ecebea;
    --sans: "Arimo", Arial, sans-serif;
    --script: "Great Vibes", cursive;
  }
  * { box-sizing: border-box; margin: 0; padding: 0; }
  html, body { width: 1200px; height: 800px; overflow: hidden; }
  body { background: var(--stage); font-family: var(--sans); position: relative; }

  .card {
    position: absolute;
    top: 241px;
    width: 555px;
    height: 318px;
    background: var(--pink);
    box-shadow: 0 6px 18px rgba(0,0,0,.18);
    overflow: hidden;
    color: var(--white);
  }
  .card--back { left: 30px; }
  .card--front { left: 615px; }

  /* Back side */
  .back__mark {
    position: absolute; left: 150px; top: 14px; width: 250px; height: 210px;
    background: radial-gradient(ellipse at center, rgba(201,48,127,.55), rgba(227,66,151,0) 70%);
  }
  .back__mark-name {
    position: absolute; left: 0; right: 0; top: 232px; text-align: center;
    font-size: 30px; font-weight: 700; color: var(--pink-deep); opacity: .55;
  }
  .services {
    position: relative; text-align: center; padding-top: 30px; line-height: 1.3;
  }
  .services__heading { font-size: 17px; font-weight: 400; }
  .services__line { font-size: 17px; font-weight: 700; }
  .services__gap { height: 34px; }

  /* Front side */
  .front__shape { position: absolute; inset: 0; }
  .front__logo {
    position: absolute; left: 52px; top: 58px; width: 230px; height: 150px; border-radius: 8px;
    background: radial-gradient(ellipse at 50% 40%, rgba(227,66,151,.45), rgba(40,40,40,.15) 60%, rgba(255,255,255,0) 80%);
  }
  .front__brand {
    position: absolute; left: 70px; top: 222px; width: 200px; text-align: center;
    color: var(--ink); font-size: 25px; font-weight: 700;
  }
  .contact { position: absolute; right: 20px; top: 20px; width: 260px; text-align: right; }
  .contact__name { font-family: var(--script), cursive; font-size: 32px; line-height: 1; }
  .contact__role { font-size: 14px; margin-top: 2px; }
  .contact__phone {
    position: absolute; right: 20px; top: 122px; font-size: 17px; font-weight: 700;
    display: flex; align-items: center; gap: 6px;
  }
  .contact__list {
    position: absolute; left: 300px; top: 226px; list-style: none; font-size: 13.5px; line-height: 1.45;
  }
  .contact__list li { display: flex; align-items: center; gap: 6px; white-space: nowrap; }
  .icon { width: 14px; height: 14px; flex: none; }
  .icon--square { width: 12px; height: 12px; background: var(--white); }
</style>
</head>
<body>

  <section class="card card--back" aria-label="Card back: services">
    <div class="back__mark" role="img" aria-label="Faint brand emblem decoration"></div>
    <p class="back__mark-name">Revels with Kit</p>
    <div class="services">
      <p class="services__heading">Function Planning</p>
      <p class="services__line">Weddings | Themed Parties | Children's Parties</p>
      <p class="services__line">Adult and Children's Photo Booths</p>
      <p class="services__line">Party Themed boxes</p>
      <div class="services__gap"></div>
      <p class="services__line">Children's costumes and accessories - Sell / Hire</p>
      <div class="services__gap"></div>
      <p class="services__line">We can find the venue, entertainment, face painters</p>
    </div>
  </section>

  <section class="card card--front" aria-label="Card front: contact">
    <svg class="front__shape" viewBox="0 0 555 318" preserveAspectRatio="none" aria-hidden="true">
      <defs>
        <linearGradient id="edgeGlow" x1="0" y1="0" x2="1" y2="0">
          <stop offset="0" stop-color="#ffffff"/>
          <stop offset="1" stop-color="#f3a6cf"/>
        </linearGradient>
      </defs>
      <path d="M0 0 H300 C360 60 372 200 318 318 H0 Z" fill="url(#edgeGlow)"/>
      <path d="M0 0 H290 C348 62 356 200 300 318 H0 Z" fill="var(--paper)"/>
    </svg>
    <div class="front__logo" role="img" aria-label="Party emblem: cocktail glass with dancers and pink stars"></div>
    <p class="front__brand">Revels with Kit</p>

    <div class="contact">
      <p class="contact__name">Rosalind Trevick</p>
      <p class="contact__role">Creative Director</p>
    </div>
    <p class="contact__phone">
      <svg class="icon" viewBox="0 0 16 16" aria-hidden="true"><path d="M3 2h3l1.5 3.5-2 1.2a8 8 0 0 0 3.8 3.8l1.2-2L14 10v3a1 1 0 0 1-1 1A11 11 0 0 1 2 3a1 1 0 0 1 1-1z" fill="none" stroke="#fff" stroke-width="1.3"/></svg>
      : 0400 555 218
    </p>
    <ul class="contact__list">
      <li><svg class="icon" viewBox="0 0 16 16" aria-hidden="true"><rect x="1.5" y="3.5" width="13" height="9" fill="none" stroke="#fff" stroke-width="1.2"/><path d="M1.5 3.5l6.5 5 6.5-5" fill="none" stroke="#fff" stroke-width="1.2"/></svg>: rosalind@revelswithkit.example</li>
      <li><svg class="icon" viewBox="0 0 16 16" aria-hidden="true"><circle cx="8" cy="8" r="6.5" fill="none" stroke="#fff" stroke-width="1.2"/><ellipse cx="8" cy="8" rx="3" ry="6.5" fill="none" stroke="#fff" stroke-width="1"/><path d="M1.5 8h13" stroke="#fff" stroke-width="1"/></svg>: www.revelswithkit.example</li>
      <li><span class="icon icon--square"></span>: Revels with Kit</li>
    </ul>
  </section>

</body>
</html>
```